BP Trifold

We need a trifold designed for Bramblecove Promotions Group. All the content and design specs are in the attached Word document. Deliver file in print-ready .ai

Industry/Entity Type

Marketing

Font styles to use
Sans Serif

Requirements
Must have
• (1) must use "product sans" font throughout entire design
• (2) on the front, the phrase "Chuck this flier in the trash if" must be large and bold. Nothing should compete with it for attention.
Should not have
• (1) do not replicate our current website as it is being redesigned
• (2) do not add content that is not in the attached word doc (like from our website).

```html
<!DOCTYPE html>
<html lang="en">
<head>
<meta charset="utf-8">
<title>Bramblecove Promotions Group – Trifold Inside</title>
<link href="https://fonts.googleapis.com/css2?family=Poppins:ital,wght@0,400;0,600;0,700;1,600;1,700&display=swap" rel="stylesheet">
<style>
  :root {
    --sky: #00aeef;
    --navy: #006a9c;
    --ink: #3a3a3a;
    --black: #111;
    --rule: #555;
    --paper: #fff;
  }
  html, body {
    margin: 0; padding: 0;
    width: 1200px; height: 1200px;
    overflow: hidden;
    background: var(--paper);
    font-family: "Poppins", sans-serif;
  }
  .canvas { position: relative; width: 1200px; height: 1200px; }
  .spread {
    position: absolute; left: 0; top: 176px;
    width: 1200px; height: 848px;
  }
  .spread-art { position: absolute; inset: 0; }
  .block { position: absolute; width: 336px; }
  .pull-quote {
    left: 34px; top: 620px;
    font-weight: 700; font-style: italic;
    font-size: 20px; line-height: 25.6px;
    color: var(--navy); text-align: justify;
  }
  .pull-quote .mark {
    font-size: 58px; line-height: 0; vertical-align: -18px;
    font-style: normal; font-weight: 700;
  }
  .section-title {
    left: 432px; top: 196px;
    font-size: 37px; line-height: 37px;
    font-weight: 700; font-style: italic;
  }
  .section-title .lead { color: var(--navy); display: block; }
  .section-title .main { color: var(--black); display: block; }
  .item-heading {
    margin: 0;
    font-size: 15.5px; line-height: 20px;
    font-weight: 600; font-style: italic;
    color: var(--navy);
  }
  .body-copy {
    margin: 0;
    font-size: 14.6px; line-height: 20px;
    color: var(--ink); text-align: justify;
  }
  .services { left: 432px; top: 320px; }
  .service + .service { margin-top: 18px; }
  .testimonials { left: 832px; top: 126px; }
  .testimonials .item-heading { margin-top: 18px; }
  .testimonials .attribution + .body-copy { margin-top: 0; }
</style>
</head>
<body>
<div class="canvas">
  <section class="spread">
    <svg class="spread-art" viewBox="0 0 1500 1060" width="1200" height="848" preserveAspectRatio="none" aria-hidden="true">
      <rect x="0" y="0" width="1500" height="1060" fill="var(--sky)"/>
      <!-- left panel white field -->
      <path d="M0,615 C80,425 270,330 470,334 L500,336 L500,1060 L0,1060 Z" fill="var(--paper)"/>
      <!-- middle & right white field -->
      <path d="M500,440 C560,270 760,95 1000,76 C1200,66 1380,100 1500,168 L1500,1060 L500,1060 Z" fill="var(--paper)"/>
      <!-- left swoosh -->
      <path d="M0,615 C70,440 260,325 470,337 C300,318 90,375 0,478 Z" fill="var(--navy)"/>
      <!-- upper swoosh -->
      <path d="M590,190 C700,110 850,50 1000,38 C1200,24 1380,58 1500,100 L1500,168 C1380,102 1200,68 1000,75 C850,82 700,130 590,190 Z" fill="var(--navy)"/>
      <!-- folds and trim -->
      <line x1="500" y1="0" x2="500" y2="1060" stroke="var(--rule)" stroke-width="1.5"/>
      <line x1="1000" y1="0" x2="1000" y2="1060" stroke="var(--rule)" stroke-width="1.5"/>
      <rect x="0.75" y="0.75" width="1498.5" height="1058.5" fill="none" stroke="var(--rule)" stroke-width="1.5"/>
    </svg>

    <p class="block pull-quote"><span class="mark">“</span> We help people find your business when they search for your services and we increase the number of website visitors that become paying customers.<span class="mark">”</span></p>

    <h2 class="block section-title"><span class="lead">Our</span><span class="main">Services</span></h2>

    <div class="block services">
      <div class="service">
        <h3 class="item-heading">Web Design and Development</h3>
        <p class="body-copy">We build custom, award-winning, persuasive websites that convert visitors into paying customers. Our websites are well worded, expertly coded, and beautifully designed to make an outstanding first impression and most importantly – to sell your services.</p>
      </div>
      <div class="service">
        <h3 class="item-heading">Search Engine Marketing</h3>
        <p class="body-copy">Using both ads and organic search techniques, when people search in Searchly, Findio, or Lookwise for your products or services, we ensure they find you above your competitors. Results are 100% guaranteed or your money back.</p>
      </div>
      <div class="service">
        <h3 class="item-heading">Social Media Marketing</h3>
        <p class="body-copy">We target the right people for your business, engage with them to create authentic conversations and interactions, and we post content and ads that drive likes, follows, comments, and shares.</p>
      </div>
    </div>

    <div class="block testimonials">
      <p class="body-copy">We’ve been working with Bramblecove Promotions Group for about 3 months. When they say they are focused on making you money, it’s no understatement! In these three months, we’ve already seen a significant increase in business -many times more than their fee- so the ROI is incredible and its easily some of the best money I could have spent on my business. Also incredible is our website… if you compare it to that of other catering companies, they really put Harborline Catering on another level! The website they made for us is beautiful, easy to use, and really drives more traffic. Bramblecove has a great process and great staff of people that REALLY know what they’re doing. If you work with them, you won’t regret it!</p>
      <h3 class="item-heading attribution">Dean Morrow, Owner &amp; Head Chef of Harborline Catering</h3>
      <p class="body-copy">Bramblecove delivers! Our leads have gone up 100%. The potential clients that have contacted our firm are serious about hiring. Teodor made the process of generating content easy and painless. I would recommend Bramblecove to anyone wanting to take their business to the next level.</p>
      <h3 class="item-heading attribution">Laura Pike, Partner at Pike &amp; Ellison Law</h3>
      <p class="body-copy">Read all of our reviews at bramblecove.example/reviews</p>
    </div>
  </section>
</div>
</body>
</html>
```